Wireless internet service provider needs flyer to lease property to build new tower sites

We need a flyer to leave behind at customer sites that we would like to turn into a tower location. We want to lease roof space or property from the customer to expand our network. We would like it to read as a sales ad that they can make up to $200/mo in exchange for signing a lease agreement with us. Attached are example photos of what typical residential tower sites look like. Contact number 530-647-1185 and email sales@brivolta.net. This will be left behind at a customer site, after a technician visits. It will be used as sales/marketing material. The flyer should be a 6x11 postcard.
Text to add to the flyer are the following points.
- Earn passive income
- Help your community get better internet
- We pay for all build costs

Target Market(s)

Rural residences

Industry/Entity Type

Internet Services

Requirements
Must have
• Sales pitch of "get paid up to $300/mo to host wireless equipment for our local rural ISP"

```html
<!DOCTYPE html>
<html lang="en">
<head>
<meta charset="utf-8">
<title>Brivolta.net – Roof Lease Flyer</title>
<link href="https://fonts.googleapis.com/css2?family=Montserrat:ital,wght@0,500;0,600;0,700;0,800;0,900;1,500;1,600&display=swap" rel="stylesheet">
<style>
  :root {
    --page-bg: #f3f3f3;
    --navy-deep: #0c1830;
    --navy: #13264a;
    --navy-soft: #1c3560;
    --red: #c3202e;
    --white: #ffffff;
  }
  * { margin: 0; padding: 0; box-sizing: border-box; }
  html, body {
    width: 1032px; height: 1200px; overflow: hidden;
    background: var(--page-bg);
    font-family: "Montserrat", sans-serif;
  }
  .flyer-frame {
    position: absolute; left: 95px; top: 12px;
    width: 751px; height: 1050px;
    transform: scale(1.12); transform-origin: 0 0;
  }
  .flyer {
    position: relative; width: 751px; height: 1050px; overflow: hidden;
    background: linear-gradient(180deg, var(--navy-deep) 0%, var(--navy) 55%, var(--navy-soft) 100%);
    color: var(--white);
  }
  .flyer-art { position: absolute; inset: 0; }

  .brand {
    position: absolute; left: 66px; top: 30px;
    display: flex; align-items: center; gap: 8px;
  }
  .brand-dot { width: 34px; height: 34px; border-radius: 50%; background: var(--red); }
  .brand-name { font-weight: 800; font-size: 27px; letter-spacing: 1px; color: var(--white); }

  .offer { position: absolute; left: 73px; top: 136px; }
  .offer-kicker { font-weight: 500; font-size: 18px; letter-spacing: 0.2px; }
  .offer-amount { font-weight: 900; font-size: 68px; line-height: 1; margin-top: 8px; letter-spacing: -1px; }
  .offer-sub { font-weight: 500; font-size: 18px; margin-top: 8px; margin-left: 4px; }

  .benefits {
    position: absolute; left: 36px; top: 500px; width: 505px;
    list-style: none;
  }
  .benefits li {
    position: relative; padding-left: 31px; margin-bottom: 7px;
    font-style: italic; font-weight: 500; font-size: 16.5px; line-height: 24px;
  }
  .benefits li::before {
    content: ""; position: absolute; left: 0; top: 5px;
    width: 15px; height: 15px; border-radius: 50%; background: var(--white);
  }
  .benefits .benefit-pitch { font-weight: 600; }

  .site-photo {
    position: absolute; left: 575px; width: 156px; height: 156px;
    border-radius: 50%; border: 4px solid var(--white);
    box-shadow: 6px 8px 14px rgba(0,0,0,0.35);
  }
  .site-photo--tower { top: 440px; background: linear-gradient(170deg, #5f8fcb 0%, #a9c4e2 60%, #7d6d55 100%); }
  .site-photo--dish { top: 618px; background: linear-gradient(160deg, #b8c2cc 0%, #6f7c8a 55%, #2b3440 100%); }
  .site-photo--roof { top: 796px; background: linear-gradient(175deg, #5d8fd6 0%, #9fc1ea 60%, #c9b79b 100%); }

  .contact-bar {
    position: absolute; left: 0; right: 0; top: 1008px; height: 30px;
    display: flex; justify-content: center; align-items: center;
    font-weight: 600; font-size: 17.5px;
  }
  .contact-item { display: flex; align-items: center; gap: 10px; padding: 0 14px; }
  .contact-item + .contact-item { border-left: 1px solid rgba(255,255,255,0.35); }
  .contact-icon { width: 22px; height: 22px; fill: none; stroke: var(--white); stroke-width: 2; }
  .contact-icon--solid { fill: var(--white); stroke: none; }
</style>
</head>
<body>
<div class="flyer-frame">
  <article class="flyer">
    <svg class="flyer-art" width="751" height="1050" viewBox="0 0 751 1050">
      <defs>
        <linearGradient id="heroPhotoTone" x1="0" y1="0" x2="1" y2="1">
          <stop offset="0" stop-color="#1a2a50"/>
          <stop offset="0.35" stop-color="#3f6fb5"/>
          <stop offset="0.65" stop-color="#8db0dc"/>
          <stop offset="0.85" stop-color="#6d7a55"/>
          <stop offset="1" stop-color="#8a6a45"/>
        </linearGradient>
        <linearGradient id="heroFade" x1="0" y1="0" x2="1" y2="0">
          <stop offset="0" stop-color="#0c1830" stop-opacity="1"/>
          <stop offset="0.3" stop-color="#0c1830" stop-opacity="0.85"/>
          <stop offset="0.55" stop-color="#0c1830" stop-opacity="0"/>
        </linearGradient>
        <linearGradient id="swooshRed" x1="0" y1="0" x2="1" y2="0">
          <stop offset="0" stop-color="#c8222f"/>
          <stop offset="0.5" stop-color="#a82418"/>
          <stop offset="1" stop-color="#8a2a0c"/>
        </linearGradient>
        <linearGradient id="footerRed" x1="0" y1="0" x2="1" y2="0">
          <stop offset="0" stop-color="#6e1c10"/>
          <stop offset="0.5" stop-color="#8e1c1e"/>
          <stop offset="1" stop-color="#7a1d0e"/>
        </linearGradient>
        <linearGradient id="bodyPhotoTone" x1="0" y1="0" x2="0" y2="1">
          <stop offset="0" stop-color="#3a4a66" stop-opacity="0.55"/>
          <stop offset="1" stop-color="#1a2a48" stop-opacity="0.15"/>
        </linearGradient>
        <clipPath id="heroClip">
          <path d="M0,0 H751 V325 C680,380 560,430 420,425 C250,420 100,320 0,170 Z"/>
        </clipPath>
      </defs>

      <g clip-path="url(#heroClip)">
        <rect x="0" y="0" width="751" height="500" fill="url(#heroPhotoTone)" role="img" aria-label="Photo of a rooftop wireless antenna mast over a rural neighbourhood under blue sky"/>
        <rect x="0" y="0" width="751" height="500" fill="url(#heroFade)"/>
      </g>

      <rect x="40" y="390" width="280" height="600" fill="url(#bodyPhotoTone)" opacity="0.6" role="img" aria-label="Faint photo of a telecom tower with antenna panels"/>

      <path d="M0,170 C100,320 250,420 420,425 C560,430 680,380 751,325 L751,332 C650,432 520,495 400,495 C250,495 100,430 0,378 Z" fill="url(#swooshRed)"/>

      <path d="M0,940 C200,1000 500,1000 751,940 V1050 H0 Z" fill="url(#footerRed)"/>
      <path d="M0,940 C200,1000 500,1000 751,940" fill="none" stroke="#b5202a" stroke-width="3"/>
    </svg>

    <header class="brand">
      <span class="brand-dot"></span>
      <span class="brand-name">BRIVOLTA.NET</span>
    </header>

    <section class="offer">
      <p class="offer-kicker">YOUR ROOF CAN EARN UPTO</p>
      <p class="offer-amount">$200/mo</p>
      <p class="offer-sub">SIMPLY SIGN A LEASE AGREEMENT</p>
    </section>

    <ul class="benefits">
      <li class="benefit-pitch">Get paid up to $300/mo to host wireless equipment for our local rural ISP.</li>
      <li>Our equipment is very low powered typically under 250mw.</li>
      <li>We take into consideration to either hide or at least make the antennas look high-tech and appealing.</li>
      <li>By entering a lease agreement, you can generate a passive income stream for yourself while also improving internet services in your area.</li>
      <li>Our towers are designed to be unobtrusive and blend in with their surroundings.</li>
      <li>We pay for all build costs.</li>
      <li>We work with you to develop an agreement that meets your specific requirements.</li>
    </ul>

    <div class="site-photo site-photo--tower" role="img" aria-label="Photo of a lattice tower beside a house"></div>
    <div class="site-photo site-photo--dish" role="img" aria-label="Photo of a dish antenna on a rooftop mast"></div>
    <div class="site-photo site-photo--roof" role="img" aria-label="Photo of rooftop antenna array"></div>

    <footer class="contact-bar">
      <span class="contact-item">
        <svg class="contact-icon" viewBox="0 0 24 24"><rect x="2" y="5" width="20" height="14"/><path d="M2,5 L12,13 L22,5"/></svg>
        sales@brivolta.net
      </span>
      <span class="contact-item">
        <svg class="contact-icon contact-icon--solid" viewBox="0 0 24 24"><path d="M6.6,2.5 L9.5,6.8 L7.6,9.2 C8.8,11.8 11.4,14.6 14.8,16.4 L17.2,14.5 L21.5,17.4 L19.5,21 C11,20.5 3.5,13 3,4.5 Z"/></svg>
        530-647-1185
      </span>
      <span class="contact-item">
        <svg class="contact-icon" viewBox="0 0 24 24"><circle cx="12" cy="12" r="9"/><ellipse cx="12" cy="12" rx="4" ry="9"/><path d="M3,12 H21 M5,7 H19 M5,17 H19"/></svg>
        www.brivolta.net
      </span>
    </footer>
  </article>
</div>
</body>
</html>
```